Brisco Home Residential cleaning services- Opening Flyer

1. I would like to have flyer design offering the hourly rate residential cleaning normal rate will be 35 AED per hour.
2. I want to have a special opening rate which is less than 25 AED which is equivalent to 30% Off.This opening offer will be limited time
We have a different cleaning packages like "Basic , Deep, And custom"
3. Also we have different types contracts Yearly/Monthly/Weekly and daily.
4. we are providing cleaning material and cleaning equipment upon request.And all the material used are environmental friendly.
5. Our customers mostly will be house wives.
6. Our service will be available in Ruwais city.
7. I would like to have a modern attractive flyer, i like it to be smart in its colors and the psychology of the customers.
8. I like to have attractive statements like " Now Available in Ruwais" and other statements from your own.
9. I will attach my logo design and if you need any other uploads let me know.
10. Our slogan is "Experience the Difference"
11. Paper size , i expect to be A5 (210mm x 148mm).
12. I am expecting the flyer to be single size as it will translated to another language in the other side.
13. please use the statement also ( less than 25 AED)
14. Do the arrangement you can see to the flyer statements as to look professional and comfortable to read.
15. Company web site is " www.briscohome.ae"
16. company email " support@briscohome.ae"
17. I will update you with contact number soon
18. My contacts are
Support@briscohome.ae
+971 508817345
+971 508817347
19. Update some slogans to be used

```html
<!DOCTYPE html>
<html lang="en">
<head>
<meta charset="utf-8">
<title>Brisco Home – Opening Flyer</title>
<link rel="stylesheet" href="https://fonts.googleapis.com/css2?family=Delius&family=Roboto:wght@300;400;500;700&family=Roboto+Condensed:wght@400;500&display=swap">
<style>
  :root {
    --brand-blue: #1a6cb3;
    --deep-blue: #0f5ea8;
    --leaf-green: #8cc63f;
    --fresh-green: #7dbb2f;
    --ink: #3d3d3d;
    --muted: #8a8a8a;
    --sky: #dcebf8;
    --paper: #ffffff;
    --backdrop: #ebe8e3;
  }
  * { box-sizing: border-box; margin: 0; padding: 0; }
  html, body { width: 1086px; height: 1200px; overflow: hidden; }
  body { background: var(--backdrop); position: relative; font-family: "Roboto", Arial, sans-serif; }

  .flyer {
    position: absolute; left: 126px; top: 10px;
    width: 834px; height: 1180px; overflow: hidden;
    background: linear-gradient(180deg, var(--sky) 0%, #f2f8fd 18%, #ffffff 55%, #eeeeee 90%);
  }
  .flyer > * { position: absolute; white-space: nowrap; }
  .artwork { left: 0; top: 0; width: 834px; height: 1180px; }

  .brand { left: 30px; top: 70px; display: flex; align-items: center; gap: 16px; }
  .brand-mark { width: 38px; height: 38px; border-radius: 50%; background: var(--leaf-green); }
  .brand-name { font-family: "Roboto", Arial, sans-serif; font-weight: 700; font-size: 48px; color: var(--brand-blue); letter-spacing: -1px; }

  .slogan { right: 18px; top: 32px; width: 410px; text-align: center; font-family: "Delius", cursive; }
  .slogan-title { font-size: 33px; font-weight: 400; color: var(--brand-blue); letter-spacing: -0.5px; }
  .slogan-title .hl { color: var(--fresh-green); }
  .slogan-title .soft { color: var(--ink); }
  .slogan-line { font-size: 21px; color: var(--ink); line-height: 34px; }
  .slogan-title + .slogan-line { margin-top: 6px; }

  .offer { left: 552px; top: 596px; width: 240px; text-align: center; color: var(--brand-blue); font-family: "Roboto", Arial, sans-serif; }
  .offer-kicker { font-size: 17px; line-height: 22px; }
  .offer-rate { font-size: 52px; font-weight: 500; line-height: 58px; margin-top: 4px; }
  .offer-rate small { font-size: 32px; }
  .offer-price { font-size: 20px; line-height: 24px; }
  .offer-note { font-size: 12px; color: var(--ink); margin-top: 4px; }

  .services-heading { left: 37px; top: 714px; font-family: "Roboto Condensed", Arial Narrow, sans-serif; font-weight: 500; font-size: 21px; color: #555; }
  .service-list { left: 44px; top: 752px; list-style: none; }
  .service { position: relative; padding-left: 54px; height: 58px; }
  .service-icon { position: absolute; left: 0; top: 2px; width: 36px; height: 36px; }
  .service-name { font-size: 25px; color: var(--fresh-green); line-height: 29px; }
  .service-tags { font-size: 17px; font-weight: 700; color: var(--deep-blue); line-height: 21px; }

  .availability { left: 555px; top: 836px; display: flex; align-items: center; gap: 16px; color: var(--brand-blue); }
  .availability-arrow { width: 48px; height: 52px; }
  .availability-text { font-size: 23px; font-weight: 700; text-align: center; line-height: 32px; }

  .supplies { left: 0; width: 834px; top: 942px; text-align: center; font-size: 17px; font-weight: 300; color: #777; line-height: 24px; }

  .phones { left: 210px; top: 996px; display: flex; align-items: center; gap: 22px; }
  .phone-icon { width: 64px; height: 52px; }
  .phone-numbers { font-size: 32px; font-weight: 500; color: var(--deep-blue); letter-spacing: 3px; line-height: 35px; }

  .contact { top: 1068px; font-size: 25px; font-weight: 700; color: var(--muted); letter-spacing: 1.5px; }
  .contact-email { left: 92px; }
  .contact-web { left: 480px; }

  .tagline-rule { left: 0; top: 1105px; width: 834px; height: 5px; background: var(--brand-blue); }
  .tagline-band { left: 0; top: 1116px; width: 834px; height: 64px; background: linear-gradient(180deg, #1f78c4, var(--deep-blue)); display: flex; align-items: center; justify-content: center; font-family: "Delius", cursive; font-size: 26px; color: #fff; letter-spacing: -0.5px; }
  .tagline-band .hl { color: var(--leaf-green); margin: 0 7px; }
</style>
</head>
<body>
<main class="flyer">
  <svg class="artwork" viewBox="0 0 834 1180" aria-hidden="true">
    <defs>
      <linearGradient id="photoTone" x1="0" y1="0" x2="1" y2="1">
        <stop offset="0" stop-color="#e4eef5"/>
        <stop offset="0.45" stop-color="#d9c4ad"/>
        <stop offset="0.75" stop-color="#c9a489"/>
        <stop offset="1" stop-color="#7ea6c6"/>
      </linearGradient>
    </defs>
    <path role="img" aria-label="Photo of a smiling family of four lying together on a bright, clean floor"
          d="M0 232 C120 262 200 262 330 222 C470 182 610 178 834 212 L834 640 C700 640 560 650 470 668 C330 695 160 690 0 600 Z"
          fill="url(#photoTone)"/>
    <path d="M0 232 C120 262 200 262 330 222 C470 182 610 178 834 205" fill="none" stroke="var(--deep-blue)" stroke-width="10"/>
    <path d="M290 226 C430 188 560 168 660 180 C740 190 800 220 834 268 L834 238 C790 200 730 176 650 170 C540 160 420 190 290 226 Z" fill="var(--leaf-green)"/>
    <path d="M0 600 C120 668 240 700 380 690 C460 684 500 672 560 660 C460 690 330 720 200 704 C110 692 40 660 0 640 Z" fill="var(--leaf-green)"/>
    <path d="M470 668 C560 650 700 638 834 648" fill="none" stroke="var(--deep-blue)" stroke-width="9"/>
    <g transform="translate(672 683)">
      <circle r="116" fill="var(--leaf-green)"/>
      <circle r="118" fill="none" stroke="var(--leaf-green)" stroke-width="8" stroke-dasharray="0.1 18.5" stroke-linecap="round"/>
      <circle r="104" fill="#ffffff"/>
      <circle r="98" fill="none" stroke="var(--leaf-green)" stroke-width="2"/>
      <line x1="-70" y1="-38" x2="70" y2="-38" stroke="#bbb" stroke-width="1" stroke-dasharray="2 3"/>
    </g>
  </svg>

  <div class="brand">
    <span class="brand-mark"></span>
    <span class="brand-name">Brisco Home</span>
  </div>

  <header class="slogan">
    <h1 class="slogan-title">Experience <span class="soft">the</span> <span class="hl">Difference</span></h1>
    <p class="slogan-line">Let us Free your time,</p>
    <p class="slogan-line">While you enjoy the thing you love</p>
  </header>

  <section class="offer">
    <p class="offer-kicker">SPECIAL</p>
    <p class="offer-kicker">OPENING OFFER</p>
    <p class="offer-rate">30% <small>off</small></p>
    <p class="offer-price">less than 25 AED</p>
    <p class="offer-note">-LIMITED TIME-</p>
  </section>

  <h2 class="services-heading">RESIDENTIAL AND COMMERCIAL CLEANING SERVICES</h2>
  <ul class="service-list">
    <li class="service">
      <svg class="service-icon" viewBox="0 0 38 38"><circle cx="19" cy="19" r="18" fill="var(--fresh-green)"/><path d="M15 11 L23 19 L15 27" fill="none" stroke="#fff" stroke-width="4.5" stroke-linecap="round" stroke-linejoin="round"/></svg>
      <p class="service-name">Hourly Rate Maid Services</p>
      <p class="service-tags">Trusted • Reliable • Professional • Legal</p>
    </li>
    <li class="service">
      <svg class="service-icon" viewBox="0 0 38 38"><circle cx="19" cy="19" r="18" fill="var(--fresh-green)"/><path d="M15 11 L23 19 L15 27" fill="none" stroke="#fff" stroke-width="4.5" stroke-linecap="round" stroke-linejoin="round"/></svg>
      <p class="service-name">Cleaning Packages</p>
      <p class="service-tags">Basic • Deep • Custom</p>
    </li>
    <li class="service">
      <svg class="service-icon" viewBox="0 0 38 38"><circle cx="19" cy="19" r="18" fill="var(--fresh-green)"/><path d="M15 11 L23 19 L15 27" fill="none" stroke="#fff" stroke-width="4.5" stroke-linecap="round" stroke-linejoin="round"/></svg>
      <p class="service-name">Services That Suits All Needs</p>
      <p class="service-tags">Daily • Weekly • Monthly • Yearly</p>
    </li>
  </ul>

  <div class="availability">
    <svg class="availability-arrow" viewBox="0 0 48 52"><path d="M30 8 C14 6 4 14 6 26 C8 34 16 38 26 38" fill="none" stroke="var(--brand-blue)" stroke-width="7" stroke-linecap="round"/><path d="M22 26 L38 38 L22 50 Z" fill="var(--brand-blue)"/></svg>
    <p class="availability-text">Now Available<br>in Ruwais</p>
  </div>

  <p class="supplies">We are providing cleaning material and cleaning equipment upon request.<br>All the material used are environmental friendly.</p>

  <div class="phones">
    <svg class="phone-icon" viewBox="0 0 64 52"><path d="M4 18 C4 6 60 6 60 18 L60 22 L46 22 L44 15 C36 12 28 12 20 15 L18 22 L4 22 Z" fill="var(--deep-blue)"/><path d="M14 24 L22 18 L42 18 L50 24 L56 48 L8 48 Z" fill="var(--deep-blue)"/><circle cx="32" cy="34" r="8" fill="#fff"/><circle cx="32" cy="34" r="4" fill="var(--deep-blue)"/></svg>
    <p class="phone-numbers">+971 508817345<br>+971 508817347</p>
  </div>

  <p class="contact contact-email">support@briscohome.ae</p>
  <p class="contact contact-web">www.briscohome.ae</p>

  <div class="tagline-rule"></div>
  <footer class="tagline-band">A CLEAN HOME IS A HEALTHY AND<span class="hl">HAPPY</span>HOME</footer>
</main>
</body>
</html>
```